New Automotive supply business in need of label designs for additive range

I need front and back label design for about 12 different variety of products. They are all to do with the Automotive additive industry such as Petrol injector cleaner, Engine Flush, Oil treatments etc. I will provide overall measurements of the label in the brief as well as examples of artwork that I like. Label must comply with local regulations, i can assist you with this. We will start with one product only, and if successful I am happy to hire you to do the remainder of the project. I would like to see designs that use my company logo colors. These products are for the workshop industry only (not retail) so does not have to be too animated.You will see my logo designs under the name "kalmor" in the uploaded files.Product Name is : Motor Prime & Renew
Front Label must say:PREPARES ENGINES FOR NEW OIL
RESTORES COMPRESSION
MINIMISES CONTAMINATION WITH NEW OIL
CONTAINS KALMOR TUFFLINE PROTECTION
RECOMMENDED FOR PETROL, DIESEL AND HYBRID ENGINES
350ML
Dimensions of metal can that will be used for label is : 175mm in height and 56mm in diameter. IN THE UPLOADED FILES YOU WILL SEE A SAMPLE OF THE ACTUAL CAN TO BE USED.
I have now included an example of a shield/guard that should be shown on the rear of the label if possible, im happy if you come up with your own shield designs.

Target Market(s)

Mechanics

Industry/Entity Type

Automotive Part

Requirements
Must have
• My logo on top
Nice to have
• Silver background
Should not have
• Pictures of engines or engine parts etc

```html
<!DOCTYPE html>
<html lang="en">
<head>
<meta charset="utf-8">
<title>Kalmor – Motor Prime &amp; Renew Label</title>
<link rel="stylesheet" href="https://fonts.googleapis.com/css2?family=Roboto:ital,wght@0,700;0,900;1,700;1,900&family=Arvo:ital,wght@1,700&display=swap">
<style>
  :root {
    --backdrop: #5e6778;
    --silver-light: #f4f5f6;
    --silver-mid: #c9ccd0;
    --silver-dark: #9a9ea4;
    --panel-dark: #2b2d31;
    --panel-mid: #4a4d53;
    --gold-deep: #c9961f;
    --gold: #e6b838;
    --gold-pale: #f6e4a6;
    --brand-blue: #1c4f9c;
    --brand-orange: #e8612a;
    --badge-rim: #8a3a1c;
    --ink: #141414;
  }
  * { margin: 0; padding: 0; box-sizing: border-box; }
  html, body {
    width: 1200px; height: 900px; overflow: hidden;
    background: var(--backdrop);
  }
  .canvas { position: relative; width: 1200px; height: 900px; }

  .label {
    position: absolute; left: 336px; top: 38px;
    width: 528px; height: 824px;
  }
  .label__shape { position: absolute; inset: 0; }

  .brand {
    position: absolute; left: 0; right: 0; top: 40px;
    display: flex; flex-direction: column; align-items: center;
  }
  .brand__mark {
    width: 92px; height: 92px; border-radius: 50%;
    background: var(--brand-blue);
    margin-bottom: 22px;
  }
  .brand__name {
    font-family: "Roboto", sans-serif; font-weight: 900;
    font-size: 38px; letter-spacing: 2px; line-height: 1;
    color: var(--brand-blue);
  }
  .brand__tagline {
    font-family: "Roboto", sans-serif; font-weight: 700;
    font-size: 11px; letter-spacing: 1px; margin-top: 5px;
    color: var(--brand-blue);
  }

  .product-name {
    position: absolute; left: 131px; top: 262px;
    width: 306px; height: 90px;
    display: flex; flex-direction: column; align-items: center; justify-content: center;
    font-family: "Arvo", serif; font-style: italic; font-weight: 700;
    font-size: 28px; line-height: 1.05; color: var(--brand-orange);
    text-transform: uppercase; text-align: center;
  }

  .claims { position: absolute; left: 34px; top: 606px; right: 30px; }
  .claims__headline {
    font-family: "Roboto", sans-serif; font-weight: 900;
    font-size: 22px; line-height: 1.15; color: var(--ink);
    text-transform: uppercase; margin-bottom: 10px;
  }
  .claims__list { list-style: none; }
  .claims__item {
    position: relative; padding-left: 20px;
    font-family: "Roboto", sans-serif; font-style: italic; font-weight: 900;
    font-size: 14.5px; line-height: 20px; color: var(--ink);
  }
  .claims__item::before {
    content: ""; position: absolute; left: 2px; top: 5px;
    width: 8px; height: 10px; background: var(--ink);
    border-radius: 50% 50% 50% 50% / 60% 60% 40% 40%;
    clip-path: polygon(50% 0, 100% 55%, 100% 100%, 0 100%, 0 55%);
  }
  .volume {
    position: absolute; left: 0; right: 0; top: 764px; text-align: center;
    font-family: "Roboto", sans-serif; font-style: italic; font-weight: 900;
    font-size: 14px; color: var(--ink);
  }
</style>
</head>
<body>
<main class="canvas">
  <section class="label">
    <svg class="label__shape" width="528" height="824" viewBox="0 0 528 824" xmlns="http://www.w3.org/2000/svg">
      <defs>
        <clipPath id="label-outline">
          <path d="M60 0 L440 0 Q528 0 528 90 L528 770 Q528 824 474 824 L60 824 Q0 824 0 770 C0 640 90 560 90 430 C90 300 10 220 10 70 Q10 0 60 0 Z"/>
        </clipPath>
        <linearGradient id="silver-field" x1="0" y1="0" x2="0" y2="1">
          <stop offset="0" stop-color="var(--silver-dark)"/>
          <stop offset="0.35" stop-color="var(--silver-light)"/>
          <stop offset="0.75" stop-color="var(--silver-light)"/>
          <stop offset="1" stop-color="var(--silver-mid)"/>
        </linearGradient>
        <linearGradient id="metal-panel" x1="0" y1="0" x2="0" y2="1">
          <stop offset="0" stop-color="var(--panel-mid)"/>
          <stop offset="1" stop-color="var(--panel-dark)"/>
        </linearGradient>
        <linearGradient id="gold-field" x1="0" y1="0" x2="0" y2="1">
          <stop offset="0" stop-color="var(--gold-deep)" stop-opacity="0"/>
          <stop offset="0.25" stop-color="var(--gold)"/>
          <stop offset="0.65" stop-color="var(--gold-pale)"/>
          <stop offset="1" stop-color="var(--gold)"/>
        </linearGradient>
        <radialGradient id="oil-glow" cx="0.58" cy="0.5" r="0.55">
          <stop offset="0" stop-color="var(--gold-pale)" stop-opacity="0.95"/>
          <stop offset="0.45" stop-color="var(--gold)" stop-opacity="0.8"/>
          <stop offset="1" stop-color="var(--gold-deep)" stop-opacity="0"/>
        </radialGradient>
        <linearGradient id="badge-fill" x1="0" y1="0" x2="0" y2="1">
          <stop offset="0" stop-color="#6a6d72"/>
          <stop offset="1" stop-color="#3a3c40"/>
        </linearGradient>
      </defs>
      <g clip-path="url(#label-outline)">
        <rect class="field-silver" width="528" height="360" fill="url(#silver-field)"/>
        <rect class="field-metal" y="330" width="528" height="300" fill="url(#metal-panel)" role="img" aria-label="Perforated metal texture"/>
        <rect class="field-gold" y="540" width="528" height="284" fill="url(#gold-field)"/>
        <rect class="oil-splash" x="60" y="340" width="468" height="300" fill="url(#oil-glow)" role="img" aria-label="Golden oil splash"/>
      </g>
      <rect class="product-badge" x="131" y="262" width="306" height="90" rx="40" ry="30"
            fill="url(#badge-fill)" stroke="var(--badge-rim)" stroke-width="3"/>
    </svg>

    <header class="brand">
      <div class="brand__mark"></div>
      <div class="brand__name">KALMOR</div>
      <div class="brand__tagline">DRIVE WITH KALMOR</div>
    </header>

    <h1 class="product-name"><span>Motor Prime</span><span>&amp; Renew</span></h1>

    <div class="claims">
      <h2 class="claims__headline">Prepares Engines<br>For New Oil</h2>
      <ul class="claims__list">
        <li class="claims__item">Restores Compression</li>
        <li class="claims__item">Minimises Contamination with New Oil</li>
        <li class="claims__item">Contains Kalmor Tuffline Protection</li>
        <li class="claims__item">Recommended For Petrol, Diesel And Hybrid Engines</li>
      </ul>
    </div>
    <p class="volume">350 ml</p>
  </section>
</main>
</body>
</html>
```